Harbor Mortgage Relief

Please help us give our website a remake or a FACELIFT. It is not very good but it says what we need it to say. But the design is terrible.
I would like our new design font and logo to be used as the theme.

I also want more photos on the site.

I also want consistency with the pages so they look clean.

We want the professionals to do this, let's see what you got!

Thank you!
Updates

Project Deadline Extended
Reason: I can understand you want to be paid. So I will commit to the fee but I want you to have time to make a KICK ASS website for me dudes! Thanks

HI!  Just wanted to say thanks for your time on these.  A lot are great.  However the firefighters have nothing to do with Foreclosure.  We are saving peoples homes from the bank taking them and selling them.   I LOVE the house photos and the families on the website.  That is the direction we like.  THanks.

THANK U ALL FOR THE WORK!   I like a few ending in the numbers: 147  733  693  536  620  478  727  508     I will go over them and choose one soon.  Thank you.   You will be paid shortly. 

Requirements
Must have
• Bright, Upbeat photos. Color scheme should be in order. We like icons on the bottom. not just text.

```html
<!DOCTYPE html>
<html lang="en">
<head>
<meta charset="utf-8">
<title>Harbor Mortgage Relief</title>
<link rel="stylesheet" href="https://fonts.googleapis.com/css2?family=Questrial&family=Montserrat:wght@600;700&display=swap">
<style>
  :root {
    --red: #d8120f;
    --red-dark: #a80c0a;
    --ink: #2a2a2a;
    --body-text: #4a4a4a;
    --muted: #6d6d6d;
    --panel-black: #0c0c0c;
    --band-dark: #2b2b2b;
    --page-light: #ececec;
    --footer-light: #f3f3f3;
    --footer-dark: #2e2e2e;
  }
  * { box-sizing: border-box; margin: 0; padding: 0; }
  html, body { width: 1190px; height: 1200px; overflow: hidden; }
  body {
    position: relative;
    font-family: "Questrial", "Century Gothic", sans-serif;
    color: var(--body-text);
    background: var(--page-light);
  }
  .header {
    position: absolute; left: 0; top: 0; width: 1190px; height: 108px;
    background: linear-gradient(#ffffff, #d9d9d9);
  }
  .stage-band {
    position: absolute; left: 0; top: 108px; width: 1190px; height: 374px;
    background: radial-gradient(ellipse at 50% 40%, #3a3a3a, #1c1c1c 80%);
  }
  .page-body {
    position: absolute; left: 0; top: 482px; width: 1190px; height: 540px;
    background: linear-gradient(#e2e2e2, #f6f6f6 40%, #f1f1f1);
  }
  .brand {
    position: absolute; left: 158px; top: 12px; display: flex; align-items: center; gap: 10px;
  }
  .brand-mark { width: 62px; height: 62px; border-radius: 50%; background: var(--red); }
  .brand-name {
    width: 170px; font-family: "Montserrat", sans-serif; font-weight: 700;
    font-size: 19px; line-height: 19px; color: var(--red); text-transform: uppercase;
  }
  .spanish {
    position: absolute; left: 629px; top: 40px;
    font-family: "Montserrat", sans-serif; font-weight: 700; font-size: 15px; color: #111;
  }
  .call-icon {
    position: absolute; left: 813px; top: 32px; width: 34px; height: 34px;
    border-radius: 5px; background: var(--red);
  }
  .call-label { position: absolute; left: 856px; top: 29px; font-size: 14px; color: #222; letter-spacing: .5px; }
  .call-number { position: absolute; left: 855px; top: 44px; font-size: 26px; color: var(--red); }
  .main-nav {
    position: absolute; left: 149px; top: 90px; width: 892px; height: 34px;
    border-radius: 12px; background: linear-gradient(#e8271f, var(--red-dark));
    box-shadow: 0 3px 4px rgba(0,0,0,.4);
  }
  .main-nav a {
    position: absolute; top: 7px; font-size: 17px; color: #1a0000; text-decoration: none;
  }
  .nav-search {
    position: absolute; left: 690px; top: 6px; width: 190px; height: 22px;
    border-radius: 11px; background: #3a0504; color: #f0d0d0; font-size: 12px;
    padding: 4px 14px;
  }
  .nav-search svg { position: absolute; right: 10px; top: 5px; }
  .hero {
    position: absolute; left: 149px; top: 139px; width: 892px; height: 359px;
    border-radius: 4px;
    background: linear-gradient(#6f8fb8 0%, #a9bfd6 30%, #7b6c4a 55%, #6a5a3c 80%, #8a7a5a 100%);
  }
  .slider-dots {
    position: absolute; left: 552px; top: 505px; display: flex; gap: 4px;
  }
  .slider-dots span { width: 9px; height: 9px; border-radius: 50%; background: #9a9a9a; }
  .slider-dots span:first-child { background: #444; }
  .welcome-title {
    position: absolute; left: 149px; top: 526px; font-size: 28px; color: var(--red); font-weight: 400;
  }
  .welcome-copy { position: absolute; left: 149px; top: 577px; width: 592px; font-size: 13.4px; line-height: 21.4px; }
  .welcome-copy p + p { margin-top: 21px; }
  .learn-more {
    position: absolute; left: 149px; top: 912px; width: 120px; height: 28px; border-radius: 14px;
    background: linear-gradient(#ffffff, #dcdcdc); box-shadow: 0 2px 3px rgba(0,0,0,.35);
    font-size: 13px; color: #333; text-align: center; line-height: 28px;
  }
  .options-panel {
    position: absolute; left: 764px; top: 524px; width: 283px; height: 456px;
    border-radius: 4px; background: var(--panel-black); overflow: hidden;
  }
  .options-panel svg.panel-top { position: absolute; left: 0; top: 0; }
  .options-intro {
    position: absolute; left: 29px; top: 16px; width: 225px;
    font-family: "Montserrat", sans-serif; font-weight: 700; font-size: 12.5px; line-height: 17px; color: #fff;
  }
  .options-list { position: absolute; left: 27px; top: 132px; width: 228px; list-style: none; }
  .options-list li {
    font-size: 13.5px; line-height: 16px; color: var(--muted);
    padding: 9px 0 10px; border-bottom: 1px solid #1f1f1f;
  }
  .options-list li:last-child { border-bottom: 0; }
  .footer-contact {
    position: absolute; left: 0; top: 1022px; width: 1190px; height: 106px;
    background: var(--footer-light); border-top: 1px solid #d0d0d0;
  }
  .tab {
    position: absolute; top: 1008px; height: 32px; padding: 0 10px; border-radius: 3px;
    background: var(--red); color: #fff; font-size: 16px; line-height: 32px;
  }
  .tab-contact { left: 149px; }
  .tab-social { left: 830px; }
  .contact-item { position: absolute; top: 1060px; display: flex; gap: 10px; align-items: center; }
  .contact-item small { display: block; font-size: 13px; color: #333; }
  .contact-item strong { display: block; font-weight: 400; font-size: 16px; color: #222; }
  .divider { position: absolute; top: 1052px; width: 1px; height: 52px; background: #cfcfcf; }
  .social { position: absolute; top: 1068px; display: flex; gap: 8px; align-items: center; font-size: 16px; color: #222; }
  .social i { width: 28px; height: 28px; border-radius: 3px; display: block; }
  .footer-base {
    position: absolute; left: 0; top: 1128px; width: 1190px; height: 72px; background: var(--footer-dark);
    text-align: center; color: #c8c8c8;
  }
  .footer-links { margin-top: 12px; font-size: 11.5px; }
  .footer-links span { margin: 0 6px; }
  .copyright { margin-top: 18px; font-size: 11px; color: #9a9a9a; }
</style>
</head>
<body>
  <header class="header">
    <div class="brand">
      <div class="brand-mark"></div>
      <div class="brand-name">Harbor Mortgage Relief</div>
    </div>
    <div class="spanish">HABLAMOS ESPANOL</div>
    <div class="call-icon">
      <svg width="34" height="34" viewBox="0 0 34 34"><path d="M11 8c2-1 3 0 4 3l1 3c0 1-1 2-2 3 1 3 3 5 6 6 1-1 2-2 3-2l3 1c3 1 4 2 3 4-1 2-3 3-5 3C15 29 5 19 5 13c0-2 3-4 6-5z" fill="#fff"/></svg>
    </div>
    <div class="call-label">CALL TOLL FREE NOW</div>
    <div class="call-number">877-555-0148</div>
  </header>

  <div class="stage-band"></div>
  <div class="page-body"></div>

  <nav class="main-nav">
    <a style="left:24px">Home</a>
    <a style="left:125px">About Us</a>
    <a style="left:254px">Services</a>
    <a style="left:377px">Contact Us</a>
    <a style="left:527px">Owner Options</a>
    <div class="nav-search">Search
      <svg width="12" height="12" viewBox="0 0 12 12"><circle cx="5" cy="5" r="3.5" stroke="#fff" stroke-width="1.6" fill="none"/><line x1="7.5" y1="7.5" x2="11" y2="11" stroke="#fff" stroke-width="1.8"/></svg>
    </div>
  </nav>

  <div class="hero" role="img" aria-label="Photo of a craftsman-style family home with a stone-pillared porch under a blue sky"></div>
  <div class="slider-dots"><span></span><span></span><span></span><span></span><span></span><span></span></div>

  <h1 class="welcome-title">Welcome to Harbor Mortgage Relief</h1>
  <div class="welcome-copy">
    <p>HARBOR MORTGAGE RELIEF specializes in assisting homeowners who are in FORECLOSURE, by offering solid alternatives to losing your home in a Trustee Sale. Having your home foreclosed on can damage your credit for up to 7 years.&nbsp; Most foreclosures end with the home owner being evicted from their home, leaving them with no money, no place to live and without ample time to safely remove their possessions from their home.&nbsp; There is no need to have this happen to you.&nbsp; No matter what part of foreclosure process you are in, WE CAN HELP!</p>
    <p>If you have received a Notice of Default (NOD) or Notice of Trustee Sale (NTS), you have options.&nbsp; Contact us today to speak to one of our licensed specialist, and let us help you put this situation behind you.</p>
    <p>We speak to hundreds of homeowners every day, we understand how frustrating this can be.&nbsp; Don't live in fear of what is to come.&nbsp; You have other options, please call or email us today and we will immediately put our specialist to work finding you a solution.</p>
  </div>
  <div class="learn-more">Learn More</div>

  <aside class="options-panel">
    <svg class="panel-top" width="283" height="135" viewBox="0 0 283 135"><polygon points="0,0 283,0 283,90 150,112 110,98 0,135" fill="var(--red)"/></svg>
    <p class="options-intro">You may not know it but there are several great options available to you.&nbsp; We can help you determine which one will work best for you FREE OF CHARGE:</p>
    <ul class="options-list">
      <li>Bringing your mortgage current to stop the foreclosure</li>
      <li>HMR can purchase your home with CASH in 7-10 days</li>
      <li>Financing/Purchase Options</li>
      <li>Relocations Assistance - if needed</li>
      <li>Remodel your home to increase it's value</li>
      <li>Many other options are available - We realize that all of our clients have different needs.&nbsp; We look at your individual needs to customize a solution just for you.</li>
    </ul>
  </aside>

  <footer>
    <div class="footer-contact"></div>
    <div class="tab tab-contact">Contact Us</div>
    <div class="tab tab-social">Stay Connected</div>

    <div class="contact-item" style="left:152px">
      <svg width="36" height="36" viewBox="0 0 34 34"><path d="M11 6c2-1 3 0 4 3l1 3c0 1-1 2-2 3 1 4 3 6 6 7 1-1 2-2 3-2l3 1c3 1 4 2 3 4-1 2-3 3-5 3C14 28 5 18 5 12c0-2 3-5 6-6z" fill="#b5b5b5"/></svg>
      <div><small>Phone</small><strong>877-555-0148</strong></div>
    </div>
    <div class="divider" style="left:332px"></div>
    <div class="contact-item" style="left:354px">
      <svg width="42" height="36" viewBox="0 0 42 36"><rect x="10" y="3" width="22" height="10" fill="#c4c4c4"/><rect x="3" y="12" width="36" height="16" rx="3" fill="#b5b5b5"/><rect x="10" y="22" width="22" height="11" fill="#d6d6d6"/></svg>
      <div><small>Fax</small><strong>+444 555 0199</strong></div>
    </div>
    <div class="divider" style="left:540px"></div>
    <div class="contact-item" style="left:558px">
      <svg width="34" height="26" viewBox="0 0 34 26"><rect x="1" y="1" width="32" height="24" rx="2" fill="#b5b5b5"/><path d="M2 3l15 12L32 3" stroke="#fff" stroke-width="2" fill="none"/></svg>
      <div><small>Email:</small><strong>info@harbormortgagerelief.com</strong></div>
    </div>

    <div class="social" style="left:832px"><i style="background:#5cb8e6"></i>Chatter</div>
    <div class="social" style="left:934px"><i style="background:#3b5a98"></i>Friendbook</div>

    <div class="footer-base">
      <div class="footer-links">Disclaimer <span>|</span> Sitemap <span>|</span> Privacy Policy</div>
      <div class="copyright">Copyright © 2012 HARBORMORTGAGERELIEF.COM. A Member of the Marlow Group. All rights reserved.</div>
    </div>
  </footer>
</body>
</html>
```